verdant manor grounds simple classy business card design

my name is owen brackley and I run a gardening business aimed at high class verdant manor grounds. the business name is verdant manor grounds and our logo was designed on brief hive .My clientel are anything from residential homes to businesses. I take pride in my work and know that I offer a service like no other in my area.
The business card will be used to represent my business and I want it to be not only rememberable, but simplistic and modern. Eye catching too. Of course I would like it relatable to gardening and appealing to the correct clientel - those being garden enthusiasts, prestigious homes and businesses that are after top of the line gardening services like no other on the market.
I am not a typical lawn mowing business so I don't want a typical card design that represents that. The gardens I work with are generally million dollar properties with owners who are very garden proud looking for upkeep and guidance from me along with sometimes whole new garden designs. I want the business cards to show to my clients that I take pride, as they do, in their garden. And I want them to know from my card that I am a professional, qualified horticulturist offering them a top of the line service for life. I want them to refer my business on. I want them to look at my business card and see class and professionalism in a modern unique bold way.
The card should be simple with the possibility of the logo on the front being embossed/debossed and my details on the back the card should have a organic garden feel it's very important to me that it is absolutely perfect
I am also very open to ideas and suggestions so look forward to seeing the designs. the business logo has been supplied with this project and I want the card to be double sided

Contact info is
Owen Brackley - Managing Director / Horticulturist
Phone : 0481 562 907
Email: owenbrackley@verdantmanorgrounds.example.au

Target Market(s)

high class gardens residential and commercial

Industry/Entity Type

Gardener

Contact Information for Business Card

Contact info is
Phone : 0481 562 907

PLEASE MAKE CARD DOUBLE SIDED

Requirements
Must have
• organic simple classy modern feel
• must flow with the current logo that has been supplied with this project
• Double sided
• Must explain in a simple way that I deal with high end gardens and I'm a qualified horticulturist
Nice to have
• embossed debossed logo
Should not have
• shouldn't be to busy or cheap looking

```html
<!DOCTYPE html>
<html lang="en">
<head>
<meta charset="utf-8">
<title>Verdant Manor Grounds – Business Card</title>
<link href="https://fonts.googleapis.com/css2?family=Cinzel:wght@400&family=Tinos:wght@400;700&display=swap" rel="stylesheet">
<style>
  :root {
    --backdrop: #e4e2dd;
    --paper: #efefed;
    --leaf-green: #629c54;
    --leaf-soft: #a9c9a0;
    --ink: #2b2b2b;
    --white: #ffffff;
  }
  html, body {
    margin: 0;
    padding: 0;
    overflow: hidden;
  }
  body {
    width: 1200px;
    height: 939px;
    background: var(--backdrop);
    position: relative;
  }
  .card {
    position: absolute;
    background: var(--paper);
    box-shadow: 0 3px 8px rgba(0,0,0,0.18);
    overflow: hidden;
  }
  .card-front { left: 154px; top: 118px; width: 429px; height: 705px; }
  .card-back  { left: 634px; top: 115px; width: 427px; height: 703px; }

  /* Front */
  .front-mark {
    position: absolute;
    left: 50%;
    top: 180px;
    width: 190px;
    height: 190px;
    margin-left: -95px;
    border-radius: 50%;
    background: var(--leaf-green);
  }
  .brand {
    position: absolute;
    left: 0;
    right: 0;
    text-align: center;
    font-family: 'Cinzel', serif;
    font-weight: 400;
    color: var(--leaf-green);
  }
  .brand-main { font-size: 35px; line-height: 1; letter-spacing: 1px; }
  .brand-sub { font-size: 22px; line-height: 1; letter-spacing: 14px; margin-top: 10px; padding-left: 14px; }
  .card-front .brand { top: 482px; }
  .front-foliage {
    position: absolute;
    left: 0;
    right: 0;
    bottom: 5px;
    height: 52px;
    background: linear-gradient(to bottom, rgba(169,201,160,0) 0%, var(--leaf-soft) 100%);
  }
  .front-edge {
    position: absolute;
    left: 0;
    right: 0;
    bottom: 0;
    height: 5px;
    background: var(--leaf-green);
  }

  /* Back */
  .back-band {
    position: absolute;
    left: 0;
    right: 0;
    top: 0;
    height: 353px;
    background: var(--leaf-green);
  }
  .back-foliage {
    position: absolute;
    left: 0;
    right: 0;
    top: 0;
    height: 60px;
    background: linear-gradient(to bottom, rgba(255,255,255,0.55) 0%, rgba(255,255,255,0) 100%);
  }
  .back-mark {
    position: absolute;
    left: 50%;
    top: 200px;
    width: 82px;
    height: 82px;
    margin-left: -41px;
    border-radius: 50%;
    background: var(--white);
  }
  .card-back .brand { top: 290px; color: var(--white); }
  .card-back .brand-main { font-size: 30px; }
  .card-back .brand-sub { font-size: 18px; letter-spacing: 12px; padding-left: 12px; margin-top: 6px; }

  .contact {
    position: absolute;
    left: 0;
    right: 0;
    top: 410px;
    text-align: center;
    font-family: 'Tinos', serif;
    color: var(--ink);
  }
  .person-name {
    font-weight: 700;
    font-size: 23px;
    color: var(--leaf-green);
    letter-spacing: 0.5px;
    margin: 0;
    line-height: 1.1;
  }
  .person-role {
    font-size: 18px;
    margin: 4px 0 0;
    letter-spacing: 0.3px;
  }
  .contact-icon {
    display: block;
    margin: 36px auto 0;
  }
  .contact-line {
    font-size: 20px;
    margin: 8px 0 0;
  }
  .contact-line.email { font-size: 17px; }
  .contact-icon.mail { margin-top: 14px; }
</style>
</head>
<body>

  <section class="card card-front" aria-label="Card front">
    <div class="front-mark"></div>
    <div class="brand">
      <div class="brand-main">VERDANT MANOR</div>
      <div class="brand-sub">GROUNDS</div>
    </div>
    <div class="front-foliage" role="img" aria-label="Row of embossed green leaves along the bottom edge"></div>
    <div class="front-edge"></div>
  </section>

  <section class="card card-back" aria-label="Card back">
    <div class="back-band">
      <div class="back-foliage" role="img" aria-label="Row of white leaves along the top edge"></div>
      <div class="back-mark"></div>
      <div class="brand">
        <div class="brand-main">VERDANT MANOR</div>
        <div class="brand-sub">GROUNDS</div>
      </div>
    </div>

    <div class="contact">
      <p class="person-name">OWEN BRACKLEY</p>
      <p class="person-role">MANAGING DIRECTOR</p>

      <svg class="contact-icon phone" width="18" height="26" viewBox="0 0 18 26" aria-hidden="true">
        <rect x="1" y="1" width="16" height="24" rx="2.5" fill="var(--leaf-green)"/>
        <rect x="3.5" y="4" width="11" height="15" fill="var(--paper)"/>
        <rect x="7" y="21" width="4" height="1.6" rx="0.8" fill="var(--paper)"/>
      </svg>
      <p class="contact-line phone">0481562907</p>

      <svg class="contact-icon mail" width="28" height="18" viewBox="0 0 28 18" aria-hidden="true">
        <rect x="1" y="1" width="26" height="16" fill="none" stroke="var(--leaf-green)" stroke-width="2"/>
        <polyline points="1,1 14,11 27,1" fill="none" stroke="var(--leaf-green)" stroke-width="2"/>
        <polyline points="1,17 10,8 M18,8 27,17" fill="none" stroke="var(--leaf-green)" stroke-width="1.5"/>
      </svg>
      <p class="contact-line email">owenbrackley@verdantmanorgrounds.example.au</p>
    </div>
  </section>

</body>
</html>
```